PACKAGING DESIGN - HOT New Brand of Haircare

We are creating a NEW haircare brand that will need to stand out on retail shelves. This is a luxury product at an affordable price. We will look for designs for 2 different formulas - Shine Boosting Shampoo & Moisturizing Conditioner containing Argan Oil and the other will be a Nourishing Shampoo & Hydrating Conditioner containing Coconut Oil.Packaging will be 32 oz bottle with pump (either Boston Round or Bullet shape). Examples are shown on the brief. This product will be sold at national retailers and needs to look like a brand that is sold at a high end boutique or salon.
Updates

Need extra days to review

Target Market(s)

Women and Men 20s - 40s who want high end hair care

Font styles to use
Sans Serif

Colors

Designer to choose colors to be used in the design.

Requirements
Must have
• Label design for the existing bottle - 4 different SKUs. (see attached brief)

```html
<!DOCTYPE html>
<html lang="en">
<head>
<meta charset="utf-8">
<title>Veyla Haircare Labels</title>
<link href="https://fonts.googleapis.com/css2?family=Josefin+Sans:wght@400;600&display=swap" rel="stylesheet">
<style>
  :root {
    --page: #ffffff;
    --label-light: #f4f4f4;
    --label-mid: #d9d9d9;
    --label-dark: #b9b9b9;
    --ink: #4a4a4a;
    --ink-soft: #5a5a5a;
    --rule: #6a6a6a;
    --brand: #ffffff;
  }
  html, body {
    margin: 0;
    padding: 0;
    width: 1200px;
    height: 1116px;
    overflow: hidden;
    background: var(--page);
    font-family: "Josefin Sans", sans-serif;
    color: var(--ink);
  }
  .canvas {
    position: relative;
    width: 1200px;
    height: 1116px;
  }
  .label {
    position: absolute;
    top: 250px;
    width: 300px;
    height: 700px;
    border-radius: 10px;
    background: linear-gradient(90deg, var(--label-dark) 0%, var(--label-light) 30%, var(--label-mid) 72%, var(--label-dark) 100%);
  }
  .label--front-coconut { left: 80px; }
  .label--back { left: 450px; text-align: center; }
  .label--front-argan { left: 820px; }

  .brand-name {
    position: absolute;
    top: 230px;
    left: 0;
    right: 0;
    text-align: center;
    font-weight: 600;
    font-size: 30px;
    letter-spacing: 4px;
    color: var(--brand);
  }
  .label--back .brand-name { top: 200px; font-size: 22px; letter-spacing: 3px; }

  .product-title {
    position: absolute;
    left: 30px;
    right: 20px;
    margin: 0;
    font-weight: 400;
    font-size: 28px;
    line-height: 1.08;
    letter-spacing: 0.5px;
    color: var(--ink-soft);
  }
  .label--front-coconut .product-title { top: 380px; }
  .label--front-argan .product-title { top: 345px; }

  .rule {
    position: absolute;
    left: 30px;
    width: 180px;
    height: 0;
    border-top: 1.5px solid var(--rule);
  }
  .label--front-coconut .rule--top { top: 450px; }
  .label--front-coconut .rule--bottom { top: 505px; }
  .label--front-argan .rule--top { top: 450px; }
  .label--front-argan .rule--bottom { top: 505px; }

  .subtitle {
    position: absolute;
    left: 30px;
    top: 461px;
    font-size: 14.5px;
    line-height: 1.35;
    font-weight: 600;
    color: var(--ink-soft);
  }
  .claims {
    position: absolute;
    left: 30px;
    top: 533px;
    width: 200px;
    font-size: 8.6px;
    line-height: 1.7;
    font-weight: 600;
    color: var(--ink-soft);
  }
  .volume {
    position: absolute;
    left: 30px;
    top: 660px;
    font-size: 20px;
    font-weight: 600;
    color: var(--ink-soft);
  }

  .back-copy {
    position: absolute;
    left: 60px;
    right: 60px;
    top: 270px;
    font-size: 7.6px;
    line-height: 1.65;
    color: var(--ink);
  }
  .back-copy h2 {
    margin: 0;
    font-size: 8px;
    font-weight: 400;
    letter-spacing: 0.3px;
  }
  .back-copy p { margin: 0 0 9px; }
  .origin {
    position: absolute;
    left: 0;
    right: 0;
    top: 670px;
    font-size: 10px;
    font-weight: 600;
  }
</style>
</head>
<body>
<main class="canvas">

  <section class="label label--front-coconut">
    <div class="brand-name">VEYLA</div>
    <h1 class="product-title">NOURISHING<br>SHAMPOO</h1>
    <div class="rule rule--top"></div>
    <div class="subtitle">&amp; Hydrating Conditioner<br>containing COCONUT OIL</div>
    <div class="rule rule--bottom"></div>
    <p class="claims">Formulated with botanical extracts to gently hydrate hair while intensely refreshing and reinvigorating dry strands paraben-free, phthalate-free, sulfate-free, color-safe for all hair types</p>
    <div class="volume">32 oz</div>
  </section>

  <section class="label label--back">
    <div class="brand-name">VEYLA</div>
    <div class="back-copy">
      <h2>DESCRIPTION</h2>
      <p>A rich and deeply hydrating shampoo that is gentle enough for daily use. Infused with moisture-attracting red algae, antioxidant argan oil and Vitamins A and E.</p>
      <h2>BENEFITS</h2>
      <p>Cleanses and helps maintain an ideal moisture balance to promote healthy-looking and manageable hair.</p>
      <h2>SUGGESTED USE</h2>
      <p>Massage through wet hair and scalp. Rinse thoroughly. Add more water to activate a rich lather. Follow with Veyla Hydrating Conditioner.</p>
      <p>Revive and restore the look of your hair with Veyla Argan Oil Repairing Shampoo. Infused with moisturizing Argan Oil, this shampoo penetrates the hair shaft, gently cleansing while repairing damage and breakage. Leaves even the most rebellious hair frizz-free, silky-soft and super glossy. Ideal for dry, damaged or color-treated hair. Free of: sulfates, parabens, phthalates, gluten, alcohol and artificial colors.</p>
    </div>
    <div class="origin">Made in USA</div>
  </section>

  <section class="label label--front-argan">
    <div class="brand-name">VEYLA</div>
    <h1 class="product-title">SHINE<br>BOOSTING<br>SHAMPOO</h1>
    <div class="rule rule--top"></div>
    <div class="subtitle">&amp; Moisturizing Conditioner<br>Containing ARGAN OIL</div>
    <div class="rule rule--bottom"></div>
    <p class="claims">Formulated with botanical extracts to gently hydrate hair while intensely refreshing and reinvigorating dry strands paraben-free, phthalate-free, sulfate-free, color-safe for all hair types</p>
    <div class="volume">32 oz</div>
  </section>

</main>
</body>
</html>
```